Musical Instrument Store Needs Band Instrument Postcard to Upgrade Current Customers

We need a new postcard design to mail to our current instrument rental customers. People start out renting a student line/beginner instrument and we want to emphasize our upgrade program that allows them to apply the equity from their beginner instrument to an intermediate or professional instrument. I have attached an image of the front (Harvey Postcard Front) and back (Harvey Postcard Back) of what we have used in the past. The back still needs to have all the information currently on it. The front can be whatever you come up with (I don't necessarily care for our current design), but should include the tagline "Reach Your Full Potential". Also, if there is more room on the front or back, it would be nice to have a brief mention of our lesson studio (I have also included our lesson studio postcard for ideas).

There are also pictures of each instrument attached. There are a few for the trumpet so you can decide which one would work best.

Target Market(s)

Current instrument rental customers

Industry/Entity Type

Store

Requirements
Must have
• The back of postcard must have all the information from the file "Harvey Postcard Back". The front should have the tagline "Reach Your Full Potential". Pictures of the instruments should be on the front as well.
Nice to have
• A brief mention or reminder that we have a large lesson studio with highly qualified instructors.

```html
<!DOCTYPE html>
<html lang="en">
<head>
<meta charset="utf-8">
<title>Marcello Music Center – Upgrade Postcard</title>
<link rel="stylesheet" href="https://fonts.googleapis.com/css2?family=Cinzel:wght@400;600;700&family=Crimson+Text:wght@400;600&display=swap">
<style>
  :root {
    --stage: #6e4a2c;
    --black: #050505;
    --gold: #e8a82a;
    --gold-light: #f2cf78;
    --olive: #7d6530;
    --white: #ffffff;
    --photo-dark: #2b2824;
    --photo-light: #cfc8bc;
  }
  * { box-sizing: border-box; margin: 0; padding: 0; }
  html, body { width: 907px; height: 1200px; overflow: hidden; }
  body { background: var(--stage); position: relative; font-family: "Crimson Text", Georgia, serif; }

  .card { position: absolute; overflow: hidden; background: var(--black); }
  .card svg.art { position: absolute; inset: 0; }

  /* Front */
  .card--front { left: 45px; top: 46px; width: 819px; height: 530px; }
  .brand-name {
    position: absolute; z-index: 2; font-family: "Cinzel", Georgia, serif; font-weight: 700;
    color: var(--white); letter-spacing: 0.5px; white-space: nowrap;
  }
  .card--front .brand-name { left: 30px; top: 326px; font-size: 25px; line-height: 28px; }
  .tagline {
    position: absolute; right: 36px; top: 412px; text-align: right;
    font-family: "Cinzel", Georgia, serif; font-weight: 600; color: var(--white);
    font-size: 42px; line-height: 46px;
  }

  /* Back */
  .card--back { left: 45px; top: 620px; width: 816px; height: 526px; }
  .section-title {
    position: absolute; left: 20px; font-family: "Cinzel", Georgia, serif; font-weight: 600;
    color: var(--gold); font-size: 19px;
  }
  .about-text {
    position: absolute; left: 20px; top: 49px; width: 428px;
    color: var(--white); font-size: 11.2px; line-height: 15px;
  }
  .lesson-list { position: absolute; left: 22px; top: 137px; width: 405px; list-style: none; }
  .lesson-list li {
    position: relative; padding-left: 16px; color: var(--white);
    font-size: 11.2px; line-height: 14px; margin-bottom: 7px;
  }
  .lesson-list li::before { content: "♪"; position: absolute; left: 0; top: 0; color: var(--gold); }
  .gift-heading {
    position: absolute; left: 0; top: 312px; width: 416px; text-align: center;
    font-family: "Cinzel", Georgia, serif; font-weight: 600; color: var(--gold);
    font-size: 19.5px; line-height: 26px;
  }
  .card--back .brand-name { left: 24px; top: 390px; font-size: 18px; line-height: 21px; }
  .contact {
    position: absolute; left: 31px; top: 445px; color: var(--white);
    font-size: 12px; line-height: 15.5px; font-style: normal;
  }
  .instrument-photo {
    position: absolute; z-index: 1; left: 222px; top: 380px; width: 240px; height: 124px;
    background: radial-gradient(ellipse at 50% 55%, #d8b25a 0%, #8c6a2a 45%, rgba(5,5,5,0) 72%);
  }
  .stamp-box {
    position: absolute; left: 743px; top: 75px; width: 41px; height: 46px;
    border: 1.5px solid #222; background: var(--white);
  }
  .address-line { position: absolute; left: 553px; width: 231px; height: 0; border-top: 1.5px solid #222; }
</style>
</head>
<body>

<section class="card card--front">
  <svg class="art" width="819" height="530" viewBox="0 0 819 530">
    <defs>
      <linearGradient id="photoTone" x1="0" y1="0" x2="1" y2="1">
        <stop offset="0" stop-color="var(--photo-dark)"/>
        <stop offset="0.55" stop-color="#7a7368"/>
        <stop offset="1" stop-color="var(--photo-light)"/>
      </linearGradient>
    </defs>
    <rect width="819" height="530" fill="var(--black)"/>
    <path role="img" aria-label="Close-up photograph of a clarinet's silver keys resting on sheet music"
          d="M0,0 H819 V150 C700,210 560,290 420,320 C270,345 120,320 0,250 Z" fill="url(#photoTone)"/>
    <path d="M819,135 V175 C680,250 560,320 430,340 C300,355 170,330 60,285 C180,320 310,330 430,305 C570,275 690,210 819,135 Z" fill="var(--gold-light)"/>
    <path d="M819,200 V260 C700,300 590,355 470,380 C330,410 190,420 0,395 V370 C180,395 320,385 460,350 C590,318 700,255 819,200 Z" fill="var(--olive)"/>
    <path d="M0,215 C60,270 170,315 300,330 C400,340 480,320 560,280 C470,345 360,365 250,360 C150,352 70,320 0,290 Z" fill="var(--gold)"/>
    <path d="M0,415 C140,440 300,430 430,395 C300,450 150,480 0,530 Z" fill="var(--gold)"/>
  </svg>
  <div class="brand-name">Marcello<br>Music Center</div>
  <h1 class="tagline">Reach Your<br>Full Potential</h1>
</section>

<section class="card card--back">
  <svg class="art" width="816" height="526" viewBox="0 0 816 526">
    <rect width="816" height="526" fill="var(--black)"/>
    <path d="M520,0 H545 C480,150 450,320 520,526 H480 C420,330 440,150 520,0 Z" fill="var(--olive)"/>
    <path d="M535,0 H552 C490,160 470,330 560,526 H530 C455,330 470,160 535,0 Z" fill="var(--gold)"/>
    <path d="M550,0 H816 V526 H555 C485,340 495,160 550,0 Z" fill="var(--gold-light)"/>
    <path d="M560,0 H816 V526 H575 C495,340 505,160 560,0 Z" fill="var(--white)"/>
  </svg>

  <h2 class="section-title" style="top:20px">About Us</h2>
  <p class="about-text">Your student is ready to Step Up to a Harvey Performance Instrument. To make it easier, you may apply equity from the instrument you are curently renting towards the upgraded Harvey Performance or Artist Series Instrument.</p>

  <h2 class="section-title" style="top:106px">Our Lesson studio</h2>
  <ul class="lesson-list">
    <li>Private, one-on-one wekly lessons for kids and adults</li>
    <li>Spacious lesson rooms</li>
    <li>Professional teachers with degrees in music or commensurate experience</li>
    <li>Performance opportunities, including recitals and ensembles</li>
    <li>Comfortable and well-appointed waiting room suitable for kids and adults</li>
    <li>Convenient Maple Grove location</li>
    <li>Lessons available for: piano, uitar, voice, drums, brasswinds, woodwinds,<br>violin, viola and cello</li>
  </ul>

  <h2 class="gift-heading">Give the Gift of Music to<br>Yourself or Someone you Love</h2>

  <div class="instrument-photo" role="img" aria-label="Photograph of a brass trumpet and trombone"></div>

  <div class="brand-name">Marcello<br>Music Center</div>
  <address class="contact">2180 Linden Ave. NW<br>Canton, OH 44720<br>330-555-0142<br>877-555-0142 (toll free)</address>

  <div class="stamp-box"></div>
  <div class="address-line" style="top:265px"></div>
  <div class="address-line" style="top:298px"></div>
  <div class="address-line" style="top:331px"></div>
</section>

</body>
</html>
```